LuMen Assembly. "Powering Enterprise Renewal" Website

I have established a new company based in Sydney Australia that exists to support large service companies to transform their businesses. I offer a bespoke alternative to the large consulting firms like QR, Ferrander, WHTC and Bramwell. My intention over time is to grow this business with more consulting partners and practitioners and expand into ASIA PAC, Europe and the US.

I would like to create a mobile responsive website that has a similar look and feel to QR, see URL below plus URLs for Bramwell, Ferrander and WHTC.

http://www.qr-example.com/
https://home.whtc-example.com/au/en/home.html
http://www.bramwell-example.com/

I am on a limited budget however so do not require a whole lot of fancy features. Key priorities;

- Responsive to all device types. PC, Tablet, Mobile
- A horizontal scrolling set of hero images that link to particular story or subject like QR-example.com. 3 only required
- Only limited content is required and most would be static apart from hero scrolling images/topics at top of page
- I would need the ability to be able to remove, replace, update the hero slides every 3-4 months
- Key priority is to present a level of professionalism and look and feel on par with QR, Ferrander, Bramwell and Co, for people to know what I do and how to contact me.
- Link site to my linked in Profile
- My logo is attached and contact details
- I have purchased the domain name www.lumenassembly-example.com.au through true registries
Updates

Industry/Entity Type

Management Consulting

Coding

Coded - Design and coding required

Number of Pages Required

1 page

Requirements
Must have
• Mobile responsive to be viewed on any device, simple clean design, easy to find contact details, 3 scrolling articles like QR-example.com that link to a PDF article. Align colours and theming to Logo on white background attached. Align fonts, look and feel etc to Log design attached

```html
<!DOCTYPE html>
<html lang="en">
<head>
<meta charset="utf-8">
<title>LuMen Assembly – Powering Enterprise Renewal</title>
<link rel="stylesheet" href="https://fonts.googleapis.com/css2?family=Lato:ital,wght@0,400;0,700;0,900;1,700;1,900&display=swap">
<style>
:root{
  --blue:#1fa3dc;
  --ink:#333333;
  --text:#4a4a4a;
  --muted:#777777;
  --rule:#dddddd;
  --panel:#e6e6e6;
  --page:#ffffff;
  --frame:#ececec;
}
*{box-sizing:border-box;margin:0;padding:0}
html,body{width:1050px;height:1200px;overflow:hidden;background:var(--page)}
body{font-family:"Lato",sans-serif;color:var(--text);position:relative}
.site{position:absolute;left:116px;top:0;width:819px;height:1200px;border-left:1px solid var(--frame);border-right:1px solid var(--frame)}
.abs{position:absolute}
a{color:inherit;text-decoration:none}

/* header */
.brand{left:126px;top:24px;display:flex;align-items:center;gap:8px}
.brand-dot{width:22px;height:22px;border-radius:50%;background:var(--blue)}
.brand-name{font-size:24px;font-weight:400;color:var(--ink);letter-spacing:.2px}
.contact{text-align:right;font-size:10px;font-weight:700;color:var(--blue);line-height:12px}
.icon{width:26px;height:26px}
.nav{display:flex;gap:21px;font-size:10px;color:var(--muted);text-transform:uppercase;letter-spacing:.2px}
.nav .active{color:var(--ink)}

/* hero */
.hero{left:126px;top:86px;width:799px;height:378px;background:linear-gradient(100deg,#2fb5e2 0%,#2a6f9e 35%,#1c4a78 55%,#c9b8b0 72%,#e7d8cf 85%,#b8a7a6 100%)}
.hero-caption{left:116px;top:230px;width:398px;height:94px;background:var(--panel);padding:10px 10px 0 10px}
.hero-title{font-size:24px;font-weight:900;color:var(--ink);line-height:26px}
.hero-text{font-size:12px;line-height:15px;color:var(--text);margin-top:3px;width:380px}
.btn{display:flex;align-items:center;padding-left:20px;font-size:9px;font-weight:900;font-style:italic;color:#fff;text-transform:uppercase;background:var(--blue);clip-path:polygon(0 0,100% 0,87% 100%,0 100%)}
.hero-arrows{left:874px;top:438px;width:51px;height:26px;background:#1b1b1b;display:flex;justify-content:space-around;align-items:center}
.dots{left:509px;top:470px;display:flex;gap:3px}
.dot{width:9px;height:9px;border-radius:50%;border:1px solid var(--blue)}
.dot.on{background:var(--blue)}
.rule{height:1px;background:var(--rule)}

/* insights */
.section-title{font-size:18px;font-weight:900;color:var(--ink);text-transform:uppercase}
.read-all{font-size:10px;font-weight:700;font-style:italic;color:var(--muted);text-transform:uppercase}
.feature-photo{left:126px;top:532px;width:388px;height:210px;background:linear-gradient(160deg,#cbd3d8 0%,#b88752 40%,#7a4320 75%,#3e2412 100%)}
.date{border-radius:50%;border:1px solid #bbb;background:#fff;display:flex;flex-direction:column;align-items:center;justify-content:center;color:var(--ink)}
.date b{font-size:16px;font-weight:400;line-height:15px}
.date small{font-size:7px;text-transform:uppercase;color:var(--muted)}
.feature-title{font-size:10.5px;font-weight:700;color:var(--blue)}
.feature-text{font-size:10.5px;line-height:14.5px;width:388px}
.post{left:536px;width:389px;height:71px}
.post .date{position:absolute;left:0;top:15px;width:42px;height:42px}
.post-body{position:absolute;left:52px;top:8px;width:337px}
.post-title{font-size:9px;font-weight:700;color:var(--blue);line-height:12px}
.post-text{font-size:8.5px;line-height:12px;color:var(--text)}

/* consulting */
.consult{left:126px;top:858px;width:799px;height:251px;background:var(--panel)}
.consult-photo{left:399px;top:858px;width:526px;height:251px;background:linear-gradient(120deg,#dfe7ee 0%,#2d3f6b 35%,#27355c 55%,#c9ced6 80%,#9aa3b0 100%)}
.consult-copy{left:137px;top:884px;width:255px}
.consult-title{font-size:18px;font-weight:900;color:var(--ink);text-transform:uppercase;line-height:20px}
.consult-sub{font-size:16.5px;font-weight:700;color:var(--ink);line-height:20px}
.consult-text{font-size:10.5px;line-height:15px;margin-top:8px}

/* footer */
.footer-bar{left:126px;top:1130px;width:799px;height:4px;background:#d6d6d6}
.legal{font-size:7.5px;color:var(--muted)}
</style>
</head>
<body>
<div class="site"></div>

<header>
  <a class="abs brand" href="#"><span class="brand-dot"></span><span class="brand-name">LuMen Assembly</span></a>
  <div class="abs contact" style="right:183px;top:19px">+61400555019<br>hello@lumenassembly-example.com.au</div>
  <svg class="abs icon" style="left:869px;top:17px" viewBox="0 0 26 26" aria-label="Message"><circle cx="13" cy="13" r="12" fill="none" stroke="#1fa3dc" stroke-width="1.5"/><path d="M7 8h12v8h-7l-3 3v-3H7z" fill="#1fa3dc"/><circle cx="10" cy="12" r="1" fill="#fff"/><circle cx="13" cy="12" r="1" fill="#fff"/><circle cx="16" cy="12" r="1" fill="#fff"/></svg>
  <svg class="abs icon" style="left:899px;top:17px" viewBox="0 0 26 26" aria-label="Professional profile"><circle cx="13" cy="13" r="12" fill="none" stroke="#1fa3dc" stroke-width="1.5"/><circle cx="13" cy="13" r="5" fill="#1fa3dc"/></svg>
  <nav class="abs nav" style="right:125px;top:57px">
    <a class="active" href="#">Home</a><a href="#">Insights</a><a href="#">Industries</a><a href="#">Services</a><a href="#">About</a><a href="#">Contact</a>
  </nav>
</header>

<section>
  <div class="abs hero" role="img" aria-label="Sailing yacht heading across a deep blue sea under a bright sky"></div>
  <div class="abs hero-caption">
    <h1 class="hero-title">FINDING THE WAY</h1>
    <p class="hero-text">Lorem ipsum dolor sit amet, consectetur adipiscing elit nam condime ntum, augue nec sollicitudin laoreet, odio urna volutpat tortor, eget viverra magna justo nec tellus maecenas sit amet mi dignissi laoreet.</p>
  </div>
  <a class="abs btn" href="#" style="left:116px;top:331px;width:113px;height:31px">&gt;&nbsp; Learn more</a>
  <div class="abs hero-arrows">
    <svg width="10" height="12" viewBox="0 0 10 12"><path d="M7 1L2 6l5 5" fill="none" stroke="#fff" stroke-width="2"/></svg>
    <svg width="10" height="12" viewBox="0 0 10 12"><path d="M3 1l5 5-5 5" fill="none" stroke="#fff" stroke-width="2"/></svg>
  </div>
  <div class="abs dots"><span class="dot on"></span><span class="dot"></span><span class="dot"></span></div>
  <div class="abs rule" style="left:126px;top:487px;width:799px"></div>
</section>

<section>
  <h2 class="abs section-title" style="left:126px;top:504px">Recent Insights</h2>
  <a class="abs read-all" href="#" style="right:125px;top:512px">&gt;&nbsp; Read all insights</a>
  <div class="abs rule" style="left:536px;top:532px;width:389px"></div>

  <div class="abs feature-photo" role="img" aria-label="Wooden chess pieces on a chessboard"></div>
  <div class="abs date" style="left:133px;top:537px;width:42px;height:42px"><b>18</b><small>Oct</small></div>
  <h3 class="abs feature-title" style="left:126px;top:749px">Lorem Ipsum Dolor Sitamet Consectetur Adipiscing Elit</h3>
  <p class="abs feature-text" style="left:126px;top:764px">Nam condimentum, augue nec sollicitudin laoreet, odio urna volutpat tortor, eget viverra magna justo nec tellus. Maecenas sit amet mi dignissim, laoreet velit ut, vehicula nunc. Cras vitae iaculis magna, vel commodo dolor etiam magna mauris...</p>

  <article class="abs post" style="top:532px">
    <div class="date"><b>15</b><small>Oct</small></div>
    <div class="post-body"><h3 class="post-title">Praesent Acrisus Sapien Laoreet Ceratac Tuismag</h3><p class="post-text">Curabitur tempor lorem vitae enim dignissim euismod. Etiam nec placerat risus. Class aptent taciti sociosqu ad litora torquent per conubia nostra, per inceptos himenaeos. Praesent dictum gravida vehicula cras commodo urna consequat finibus malesuada...</p></div>
  </article>
  <div class="abs rule" style="left:536px;top:603px;width:389px"></div>
  <article class="abs post" style="top:603px">
    <div class="date"><b>13</b><small>Oct</small></div>
    <div class="post-body"><h3 class="post-title">Quisque Ametus Interdum Eratligula Scelerisque</h3><p class="post-text">Suspendisse accumsan ullamcorper aliquam. Nullam in libero sapien. Aenean dui purus, tristique id congue a, convallis non sem. Ut turpis dui, consectetur id urna ac, tincidunt volutpat quam quis lacus eu diam semper sagittis ut a orci class aptent...</p></div>
  </article>
  <div class="abs rule" style="left:536px;top:674px;width:389px"></div>
  <article class="abs post" style="top:674px">
    <div class="date"><b>8</b><small>Oct</small></div>
    <div class="post-body"><h3 class="post-title">Donec Tempor Ondimentum Huspendliqua</h3><p class="post-text">Fusce efficitur pharetra molestie. Maecenas odio ligula, mattis non orci sit amet, tempor ultrices massa. Pellentesque habitant morbi tristique senectus et netus et malesuada fames ac turpis egestas. Suspendisse varius at mauris sed volutpat...</p></div>
  </article>
  <div class="abs rule" style="left:536px;top:746px;width:389px"></div>
  <article class="abs post" style="top:744px">
    <div class="date"><b>5</b><small>Oct</small></div>
    <div class="post-body"><h3 class="post-title">Vivamus Ante Kretra Wjusto Tbibendum Gccumsan Maselluet</h3><p class="post-text">Etiam ipsum orci, convallis non ante eleifend, pretium fermentum purus. Nullam imperdiet tristique elit, nec tincidunt tortor commodo eget. Quisque convallis tellus vel urna scelerisque, in sagittis tortor cursus. Vivamus venenatis tincidunt ligula ut...</p></div>
  </article>
  <div class="abs rule" style="left:536px;top:814px;width:389px"></div>
  <div class="abs rule" style="left:126px;top:836px;width:799px"></div>
</section>

<section>
  <div class="abs consult"></div>
  <div class="abs consult-photo" role="img" aria-label="Business people in suits reviewing charts on a tablet at a desk"></div>
  <div class="abs consult-copy">
    <h2 class="consult-title">Consulting Service</h2>
    <p class="consult-sub">LuMen, Empower, Tramsform, Enable, and Grow</p>
    <p class="consult-text">Lorem ipsum dolor sit amet, consectetur adipiscing elit. Nam condimentum, augue nec sollicitudin laoreet, odio urna volutpat tortor, eget viverra magna justo nec tellus. Maecenas sit amet mi dignissim, laoreet velit ut, vehicula nunc. Cras vitae iaculis magna, vel commodo dolor etiam magna mauris hendrerit ac lacus id titor.</p>
  </div>
  <a class="abs btn" href="#" style="left:116px;top:1046px;width:113px;height:32px">&gt;&nbsp; Contact us</a>
</section>

<footer>
  <div class="abs footer-bar"></div>
  <nav class="abs nav" style="left:126px;top:1153px"><a class="active" href="#">Home</a><a href="#">Insights</a><a href="#">Industries</a><a href="#">Services</a><a href="#">About</a><a href="#">Contact</a></nav>
  <p class="abs legal" style="left:126px;top:1172px">©2016 LuMen Assembly. &nbsp;|&nbsp; Terms &amp; Conditions</p>
  <div class="abs contact" style="right:183px;top:1153px">+61400555019<br>hello@lumenassembly-example.com.au</div>
  <svg class="abs icon" style="left:869px;top:1151px" viewBox="0 0 26 26" aria-label="Message"><circle cx="13" cy="13" r="12" fill="none" stroke="#1fa3dc" stroke-width="1.5"/><path d="M7 8h12v8h-7l-3 3v-3H7z" fill="#1fa3dc"/><circle cx="10" cy="12" r="1" fill="#fff"/><circle cx="13" cy="12" r="1" fill="#fff"/><circle cx="16" cy="12" r="1" fill="#fff"/></svg>
  <svg class="abs icon" style="left:899px;top:1151px" viewBox="0 0 26 26" aria-label="Professional profile"><circle cx="13" cy="13" r="12" fill="none" stroke="#1fa3dc" stroke-width="1.5"/><circle cx="13" cy="13" r="5" fill="#1fa3dc"/></svg>
</footer>
</body>
</html>
```